Local Roofing/Construction company business needs new biz card design

We need a new business card design, current cards are from the start of this operation and generic at best. We are a local Construction Company (General Contractor) with a majority of our work originating from insurance claims-exterior finish work is the main focus (Roofs-Siding-Gutters etc). Heavily involved with homeowners and the low ball offers they receive from insurance company's after a insurable event takes place. I have attached some of our original logo file(s) below.

```html
<!DOCTYPE html>
<html lang="en">
<head>
<meta charset="UTF-8">
<title>Stonebridge Builders — Business Card</title>
<link href="https://fonts.googleapis.com/css2?family=Montserrat:wght@400;500;700;800&display=swap" rel="stylesheet">
<style>
  :root {
    --page: #1b1b1d;
    --card: #232323;
    --accent: #22d46f;
    --white: #ffffff;
    --text-soft: #d9d9d9;
    --mark-dark: #2c2c2e;
  }
  * { box-sizing: border-box; margin: 0; padding: 0; }
  html, body {
    width: 1200px; height: 900px; overflow: hidden;
    background: var(--page);
    font-family: "Montserrat", sans-serif;
  }
  .canvas {
    position: relative; width: 1200px; height: 900px;
  }
  .card {
    position: absolute; left: 260px;
    width: 680px; height: 388px;
    background: var(--card);
    border-radius: 22px;
    border-bottom: 5px solid var(--accent);
    overflow: hidden;
  }
  .card--front { top: 50px; }
  .card--back { top: 462px; }

  .brand {
    display: flex; align-items: center; gap: 18px;
  }
  .brand__square {
    width: 46px; height: 46px; background: var(--accent); flex: none;
  }
  .brand__name {
    color: var(--white);
    font-weight: 800;
    text-transform: uppercase;
    letter-spacing: 2px;
    line-height: 1.05;
  }
  .card--front .brand {
    position: absolute; left: 50%; top: 50%;
    transform: translate(-50%, -50%);
  }
  .card--front .brand__name { font-size: 40px; }

  .card--back .brand {
    position: absolute; left: 48px; top: 46px;
  }
  .card--back .brand__name { font-size: 34px; }

  .contact {
    position: absolute; left: 48px; top: 170px;
    padding-left: 20px;
    border-left: 5px solid var(--accent);
  }
  .contact__name {
    color: var(--accent); font-weight: 700; font-size: 24px;
  }
  .contact__role {
    color: var(--text-soft); font-size: 14px; margin-top: 2px;
  }
  .contact__address {
    color: var(--text-soft); font-size: 14px; line-height: 1.4;
    margin-top: 18px;
  }
  .contact__list {
    list-style: none; margin-top: 16px;
  }
  .contact__list li {
    display: flex; align-items: center; gap: 10px;
    color: var(--text-soft); font-size: 14px; line-height: 1.6;
  }
  .contact__list svg { width: 13px; height: 13px; flex: none; }

  .decor-mark {
    position: absolute; right: 70px; top: 80px;
    width: 220px; height: 220px;
    background: linear-gradient(135deg, #3a3a3c, var(--mark-dark) 60%, #1e1e1f);
    border-radius: 4px;
  }
</style>
</head>
<body>
<main class="canvas">

  <section class="card card--front" aria-label="Card front">
    <div class="brand">
      <span class="brand__square"></span>
      <span class="brand__name">Stonebridge Builders</span>
    </div>
  </section>

  <section class="card card--back" aria-label="Card back">
    <div class="brand">
      <span class="brand__name">Stonebridge<br>Builders</span>
    </div>

    <div class="contact">
      <p class="contact__name">Daniel Harper</p>
      <p class="contact__role">Owner</p>
      <p class="contact__address">42 Cedar Hollow Ln<br>Maple Ridge, MO 63012</p>
      <ul class="contact__list">
        <li>
          <svg viewBox="0 0 24 24" aria-hidden="true"><path fill="#22d46f" d="M6.6 10.8a15 15 0 0 0 6.6 6.6l2.2-2.2a1 1 0 0 1 1-.25 11.4 11.4 0 0 0 3.6.57 1 1 0 0 1 1 1V20a1 1 0 0 1-1 1A17 17 0 0 1 3 4a1 1 0 0 1 1-1h3.5a1 1 0 0 1 1 1c0 1.25.2 2.45.57 3.57a1 1 0 0 1-.25 1z"/></svg>
          555-204-7318
        </li>
        <li>
          <svg viewBox="0 0 24 24" aria-hidden="true"><path fill="#22d46f" d="M2 5h20v14H2z"/><path fill="none" stroke="#232323" stroke-width="2" d="M2 5l10 8 10-8"/></svg>
          info@stonebridgebuild.com
        </li>
        <li>
          <svg viewBox="0 0 24 24" aria-hidden="true"><circle cx="12" cy="12" r="10" fill="#22d46f"/><path fill="none" stroke="#232323" stroke-width="1.6" d="M2 12h20M12 2c3 3 3 17 0 20M12 2c-3 3-3 17 0 20"/></svg>
          www.stonebridgebuild.com
        </li>
      </ul>
    </div>

    <div class="decor-mark" role="img" aria-label="Large dark glossy brand mark decoration"></div>
  </section>

</main>
</body>
</html>
```